We are looking for a simple design that would be uplifting for
upscale drug addicts

MERIDIAN COLLECTIVE

PLEASE SEE THE LINK FOR TAG LINE AND CONTENT

thank you.

here is all the actual info we need and we want something like this...

http://files.qzr.lumtrabox.example/rest/objects/7c2910e4b557d81a93e40bd59fa644163fe2adf0899f?uid=bdf8e1b9b6f556b6b83c44471fdc79%2fproofs&expires=1482716603&signature=kT9PwLmQxZbVoNHLdtrtlmoGHQB%3d

The shape and colors don't have to be like what I posted it is only an example.

Target Market(s)

Harlow Row, internet and creative types, men, early 30's,
upwardly mobile, drug addicts

current site

brightkestrelway.example

now launching new name Meridian Collective

Industry/Entity Type

Drug

Requirements
Must have
• upscale look, great font
Should not have
• a corporate look but should not look like a clinic.

```html
<!DOCTYPE html>
<html lang="en">
<head>
<meta charset="utf-8">
<title>Meridian Collective – Business Card</title>
<link href="https://fonts.googleapis.com/css2?family=Arimo:ital,wght@0,400;0,700;1,400&family=Oxygen:wght@400&display=swap" rel="stylesheet">
<style>
  :root {
    --backdrop: #2b2b2b;
    --card-top: #ffffff;
    --card-bottom: #dcdddf;
    --ink: #1d1d1d;
    --ink-soft: #3a3a3a;
    --brand-red: #d3141c;
    --brand-red-bright: #ec1c24;
    --brand-red-deep: #930b10;
    --swoosh-grey: #7d7e80;
    --swoosh-light: #c9cacc;
    --paper-white: #ffffff;
  }
  html, body {
    margin: 0;
    width: 1200px;
    height: 909px;
    overflow: hidden;
    background: var(--backdrop);
  }
  .business-card {
    position: absolute;
    left: 50px;
    top: 137px;
    width: 1100px;
    height: 635px;
    box-shadow: 0 12px 30px rgba(0,0,0,0.45);
  }
  .business-card svg { display: block; width: 100%; height: 100%; }
  .person-name { font-family: "Arimo", Arial, sans-serif; font-weight: 700; font-size: 28px; fill: var(--ink); }
  .person-credential { font-weight: 400; }
  .person-role { font-family: "Arimo", Arial, sans-serif; font-style: italic; font-size: 16px; fill: var(--ink-soft); }
  .contact-line { font-family: "Arimo", Arial, sans-serif; font-size: 13.5px; fill: var(--ink); }
  .brand-name { font-family: "Oxygen", sans-serif; font-size: 29px; fill: #333333; letter-spacing: 0.5px; }
  .tagline { font-family: "Oxygen", sans-serif; font-size: 16px; fill: var(--paper-white); letter-spacing: 0.3px; }
  .icon { fill: var(--brand-red); }
</style>
</head>
<body>
<div class="business-card">
  <svg viewBox="0 0 714 412" xmlns="http://www.w3.org/2000/svg" aria-label="Meridian Collective business card for Daniel Morrow">
    <defs>
      <linearGradient id="card-face" x1="0" y1="0" x2="0" y2="1">
        <stop offset="0" stop-color="var(--card-top)"/>
        <stop offset="1" stop-color="var(--card-bottom)"/>
      </linearGradient>
      <linearGradient id="red-band" x1="0" y1="0" x2="1" y2="0">
        <stop offset="0" stop-color="var(--brand-red)"/>
        <stop offset="0.45" stop-color="var(--brand-red-bright)"/>
        <stop offset="1" stop-color="var(--brand-red-deep)"/>
      </linearGradient>
      <linearGradient id="grey-band" x1="0" y1="0" x2="1" y2="0">
        <stop offset="0" stop-color="var(--swoosh-grey)"/>
        <stop offset="0.4" stop-color="var(--swoosh-light)"/>
        <stop offset="1" stop-color="var(--swoosh-grey)"/>
      </linearGradient>
      <linearGradient id="mark-fill" x1="0" y1="0" x2="0" y2="1">
        <stop offset="0" stop-color="var(--brand-red-bright)"/>
        <stop offset="1" stop-color="var(--brand-red-deep)"/>
      </linearGradient>
    </defs>

    <rect class="card-face" width="714" height="412" fill="url(#card-face)"/>

    <!-- swoosh bands -->
    <path class="swoosh-grey" fill="url(#grey-band)" d="M0,312 Q160,345 330,335 Q450,327 530,306 Q420,346 260,362 Q120,370 0,368 Z"/>
    <path class="swoosh-divider" fill="var(--paper-white)" d="M0,368 Q300,360 530,306 Q600,290 714,248 L714,252 Q420,352 0,372 Z"/>
    <path class="swoosh-red" fill="url(#red-band)" d="M0,372 Q420,352 714,250 L714,412 L0,412 Z"/>

    <!-- name block -->
    <polygon class="name-pointer" fill="var(--brand-red)" points="0,105 34,122 0,140"/>
    <text class="person-name" x="52" y="125">Daniel Morrow, <tspan class="person-credential">CASAC</tspan></text>
    <text class="person-role" x="124" y="150">Program Coordinator</text>

    <!-- brand -->
    <rect class="brand-square" x="531" y="27" width="57" height="57" fill="url(#mark-fill)" stroke="var(--brand-red-deep)" stroke-width="1.5"/>
    <text class="brand-name" x="694" y="126" text-anchor="end">MERIDIAN</text>
    <text class="brand-name" x="694" y="152" text-anchor="end" style="font-size:22px">COLLECTIVE</text>

    <!-- contact details -->
    <g class="contact-details">
      <path class="icon" d="M53,195 L59,189 L65,195 L63,195 L63,201 L55,201 L55,195 Z"/>
      <text class="contact-line" x="72" y="201">418 Harlow Row Suite 302</text>
      <text class="contact-line" x="72" y="217">Eastbridge, NY 10427</text>

      <path class="icon" d="M54,230 Q54,228 56,228 L58,231 L57,233 Q59,236 61,237 L63,236 L66,238 Q66,241 63,241 Q55,239 54,230 Z"/>
      <text class="contact-line" x="72" y="240">555.014.2830</text>

      <rect class="icon" x="55" y="254" width="9" height="3"/>
      <rect class="icon" x="53" y="258" width="13" height="5" rx="1"/>
      <rect class="icon" x="56" y="264" width="7" height="3"/>
      <text class="contact-line" x="72" y="263">555.014.2831</text>

      <rect class="icon" x="53" y="281" width="13" height="8"/>
      <path d="M53,281 L59.5,286 L66,281" fill="none" stroke="#ffffff" stroke-width="1"/>
      <text class="contact-line" x="72" y="287">counselor@ashgrovehealth.example</text>

      <circle cx="59.5" cy="306" r="5.5" fill="none" stroke="var(--brand-red)" stroke-width="1.4"/>
      <path d="M54,306 H65 M59.5,300.5 V311.5" stroke="var(--brand-red)" stroke-width="1"/>
      <text class="contact-line" x="72" y="310">www.brightkestrelway.example</text>
    </g>

    <!-- tagline -->
    <text class="tagline" x="695" y="365" text-anchor="end">We don’t cut any corners</text>
    <text class="tagline" x="695" y="385" text-anchor="end">when it comes to your longterm recovery</text>
  </svg>
</div>
</body>
</html>
```